Comprehensive online math curriculum teaching service needs a PowerPoint design

We need a PowerPoint presentation for a startup company based in Edmonton, Alberta, Canada, called Brivento Numérica. Brivento Numérica is a comprehensive online math curriculum teaching service for independently schooled students in grades 6 through 12 worldwide. Teaching is done through a one-on-one, virtual adaptive classroom that uses integrated, interactive digital whiteboards for both teachers and students, with a standard modular lesson workflow for mastering math. Brivento Numérica is designed to help students from all socioeconomic backgrounds master mathematics. The creative brief also includes our logo.
Updates
Target Market(s)
Independently schooled students in grades 6 through 12 worldwide
Industry/Entity Type
Education - Mathematics Teaching
Look and feel
Each slider illustrates characteristics of the customer's brand and the style your logo design should communicate.

```html
<!DOCTYPE html>
<html lang="en">
<head>
<meta charset="utf-8">
<title>Brivento Numérica – Presentation Overview</title>
<link href="https://fonts.googleapis.com/css2?family=Outfit:wght@500;600;700&family=Montserrat:wght@400;500;600;700&display=swap" rel="stylesheet">
<style>
:root{
  --stage:#a7a7a7;
  --slide:#efefef;
  --teal:#27998b;
  --ink:#141414;
  --text:#444;
  --muted:#666;
  --line:#dcdcdc;
  --white:#fff;
}
*{margin:0;padding:0;box-sizing:border-box}
html,body{width:992px;height:1200px;overflow:hidden}
body{background:var(--stage);font-family:"Montserrat",sans-serif;color:var(--text);position:relative}
.slide{position:absolute;width:449px;height:252px;background:var(--slide);box-shadow:0 6px 14px rgba(0,0,0,.25);overflow:hidden}
.col-l{left:32px}.col-r{left:511px}
.row-1{top:35px}.row-2{top:326px}.row-3{top:617px}.row-4{top:908px}
.abs{position:absolute}
.title{position:absolute;left:0;width:100%;text-align:center;font-family:"Outfit",sans-serif;font-weight:600;color:var(--ink);font-size:11.5px;letter-spacing:.1px}
.rule{position:absolute;left:50%;width:83px;height:2px;margin-left:-41.5px;background:var(--teal);border-radius:1px}
.footer{position:absolute;left:19px;top:224px;width:404px;height:22px;background:var(--white);border-radius:11px;display:flex;align-items:center;justify-content:space-between;padding:0 13px 0 8px}
.brand{display:flex;align-items:center;gap:3px;font-weight:500;color:var(--ink)}
.brand-dot{border-radius:50%;background:var(--teal);display:inline-block}
.footer .brand{font-size:5px}
.footer .brand-dot{width:6px;height:6px}
.copy{font-size:4.3px;font-weight:600;color:var(--ink)}
.page-num{position:absolute;left:431px;top:229px;width:12px;height:12px;border-radius:50%;background:var(--teal);color:#fff;font-size:4.3px;font-weight:700;display:flex;align-items:center;justify-content:center}
.ticks{list-style:none}
.ticks li{position:relative;padding-left:11px;font-size:6px;line-height:9.3px}
.ticks li::before{content:"";position:absolute;left:0;top:2px;width:5px;height:5px;border-radius:50%;background:var(--teal)}
.ticks li::after{content:"";position:absolute;left:1.6px;top:3.1px;width:1.4px;height:2.2px;border:solid #fff;border-width:0 .7px .7px 0;transform:rotate(45deg)}
/* whiteboard artwork placeholder */
.board-art{position:absolute;left:0;top:0;width:449px;height:252px;background:radial-gradient(ellipse at 50% 45%,#ffffff 0%,#ffffff 62%,#e4e4e4 82%,#cfcfcf 100%)}
.board-logo{position:absolute;left:0;width:100%;display:flex;flex-direction:column;align-items:center}
.board-logo .brand{font-size:7px}
.board-logo .brand-dot{width:7px;height:7px}
.tagline{font-size:2.8px;color:var(--muted);margin-top:1px;margin-left:10px}
.photo{position:absolute;left:232px;top:66px;width:191px;height:136px;border:3px solid var(--teal);border-radius:12px;background:linear-gradient(135deg,#dfe6e2 0%,#c9bfae 45%,#58627a 75%,#e9e4dc 100%)}
.pillar{position:absolute;top:96px;width:108px;height:108px;border-radius:50%;background:var(--teal);border:2px solid #fff;display:flex;flex-direction:column;align-items:center;justify-content:center;color:#fff;text-align:center;font-size:6px;font-weight:600;line-height:9.3px;padding:0 18px}
.pillar svg{width:24px;height:24px;margin-bottom:7px}
.table-box{position:absolute;left:25px;top:39px;width:398px;height:176px;background:#fff;border:1px solid var(--line);border-radius:10px}
.th{position:absolute;top:5px;height:16px;border-radius:8px;background:var(--teal);color:#fff;font-size:6px;font-weight:600;display:flex;align-items:center}
.trow{position:absolute;left:14px;width:378px;height:25px;border-bottom:1px solid #e6e6e6;display:flex;align-items:center}
.trow:last-child{border-bottom:none}
.trow .ico{width:30px;display:flex;justify-content:center}
.trow .ico svg{width:11px;height:11px}
.trow .feat{width:70px;font-size:4.6px;font-weight:600;color:var(--ink);line-height:6px;height:100%;display:flex;align-items:center;border-right:1px solid #e6e6e6}
.trow .desc{flex:1;font-size:3.9px;line-height:5.2px;color:var(--text);padding-left:6px}
.step{position:absolute;top:83px;width:70px;margin-left:-35px;text-align:center}
.step-ring{width:50px;height:50px;margin:0 auto;border-radius:50%;background:#fff;border:2px solid #ddd;display:flex;align-items:center;justify-content:center}
.step-ring svg{width:22px;height:22px}
.step h4{font-size:5.5px;font-weight:600;color:var(--ink);margin-top:8px;line-height:8px}
.step p{font-size:5.3px;color:var(--muted);line-height:8px;margin:2px auto 0;width:58px}
.arrow{position:absolute;top:105px;width:16px;height:6px}
.card{position:absolute;top:50px;width:195px;height:157px;background:#fff;border:1px solid var(--line);border-radius:10px;padding:7px 8px}
.card-head{height:17px;border-radius:9px;background:var(--teal);color:#fff;font-family:"Outfit",sans-serif;font-weight:600;font-size:8.3px;display:flex;align-items:center;justify-content:center}
.card .ticks{margin:14px 0 0 12px}
.card .ticks li{margin-bottom:9.5px}
</style>
</head>
<body>

<section class="slide col-l row-1">
  <div class="board-art" role="img" aria-label="Illustration of a classroom whiteboard with coloured magnets, markers and a sponge on its tray"></div>
  <div class="board-logo" style="top:42px">
    <div class="brand"><span class="brand-dot"></span>Brivento Numérica</div>
    <div class="tagline">Inspiring Math • Empowering Learning</div>
  </div>
  <div class="title" style="top:94px;font-size:15px">Brivento Numérica</div>
  <div class="rule" style="top:114px;width:50px;margin-left:-25px"></div>
  <p class="abs" style="left:86px;top:124px;width:276px;text-align:center;font-size:6px;line-height:9.3px">A comprehensive online math curriculum teaching service for independently schooled students in grades 6 through 12 worldwide. Teaching is done through our math academy, a one-on-one, virtual, adaptive classroom that uses integrated, interactive digital whiteboards for both teachers and students, with a standard, modular lesson workflow for mastering math.</p>
  <p class="abs" style="left:0;width:449px;top:183px;text-align:center;font-size:4.4px;font-weight:700;color:var(--ink)">Dr. Elena Marwick | Founder &amp; Lead Teacher</p>
</section>

<section class="slide col-l row-2">
  <div class="title" style="top:16px">The Problem in Digital Math Education</div>
  <div class="rule" style="top:33px"></div>
  <ul class="ticks abs" style="left:25px;top:71px;width:190px">
    <li style="margin-bottom:9.5px">Current online tools are not built for math</li>
    <li style="margin-bottom:9.5px">Lack of comprehensive math curricula based on incremental and modular lesson plans aimed at mastery of math skills</li>
    <li style="margin-bottom:9.5px">Students lose focus without visual, hands-on interaction</li>
    <li style="margin-bottom:9.5px">Teachers struggle to explain concepts without a whiteboard</li>
    <li style="margin-bottom:9.5px">Existing whiteboards lack math-specific tools and structure</li>
    <li>Feedback is delayed, and collaboration is limited</li>
  </ul>
  <div class="photo" role="img" aria-label="Photo of a frustrated student holding his head over an open book at a desk"></div>
  <footer class="footer"><div class="brand"><span class="brand-dot"></span>Brivento Numérica</div><span class="copy">© Copyrights 2026 | All Rights Reserved</span></footer>
  <span class="page-num">02</span>
</section>

<section class="slide col-l row-3">
  <div class="abs" style="left:0;width:449px;top:18px;text-align:center;font-size:6px;font-weight:600;color:var(--teal)">Brivento Numérica</div>
  <div class="title" style="top:26px;font-size:10.5px;line-height:13px">A Purpose-Built Comprehensive Math Curriculum<br>Virtual Teaching Service</div>
  <div class="rule" style="top:56px"></div>
  <p class="abs" style="left:0;width:449px;top:63px;text-align:center;font-size:6px;line-height:9.3px">Brivento Numérica brings teachers and students together in an interactive, real-time virtual math classroom.<br>Brivento Numérica delivers a pedagogical approach for rapid mastery of mathematical concepts and skills.</p>
  <div class="pillar" style="left:26px">
    <svg viewBox="0 0 24 24" fill="#fff"><rect x="2" y="3" width="20" height="13" rx="1"/><rect x="11" y="1" width="2" height="3"/><path d="M7 16l-3 7h2l3-7zM17 16l3 7h-2l-3-7z"/><rect x="5" y="7" width="9" height="1.6" fill="#27998b"/><rect x="5" y="10.5" width="6" height="1.6" fill="#27998b"/></svg>
    Collaborative digital whiteboards</div>
  <div class="pillar" style="left:122px">
    <svg viewBox="0 0 24 24" fill="#fff"><rect x="4" y="1" width="16" height="22" rx="2"/><rect x="7" y="4" width="10" height="4" fill="#27998b"/><g fill="#27998b"><rect x="7" y="10" width="2.5" height="2.5"/><rect x="10.8" y="10" width="2.5" height="2.5"/><rect x="14.5" y="10" width="2.5" height="2.5"/><rect x="7" y="14" width="2.5" height="2.5"/><rect x="10.8" y="14" width="2.5" height="2.5"/><rect x="14.5" y="14" width="2.5" height="2.5"/><rect x="7" y="18" width="2.5" height="2.5"/><rect x="10.8" y="18" width="6.2" height="2.5"/></g></svg>
    Math-specific<br>tools</div>
  <div class="pillar" style="left:218px">
    <svg viewBox="0 0 24 24" fill="#fff"><circle cx="12" cy="4" r="3.5"/><path d="M3 11l9 3 9-3v10l-9 3-9-3z"/><circle cx="3" cy="15" r="1.5"/><circle cx="21" cy="15" r="1.5"/></svg>
    Teacher-student workspaces and live feedback</div>
  <div class="pillar" style="left:314px">
    <svg viewBox="0 0 24 24" fill="#fff"><rect x="1" y="1" width="10" height="10" rx="1.5"/><rect x="13" y="1" width="10" height="10" rx="1.5"/><rect x="1" y="13" width="10" height="10" rx="1.5"/><rect x="13" y="13" width="10" height="10" rx="1.5"/><g stroke="#27998b" stroke-width="1.6"><path d="M6 3.5v5M3.5 6h5M15.5 6h5M3.8 15.8l4.4 4.4M8.2 15.8l-4.4 4.4M15.5 16.5h5M15.5 19.5h5"/></g></svg>
    Comprehensive curricula designed for rapid mastery of math</div>
  <footer class="footer"><div class="brand"><span class="brand-dot"></span>Brivento Numérica</div><span class="copy">© Copyrights 2026 | All Rights Reserved</span></footer>
  <span class="page-num">03</span>
</section>

<section class="slide col-l row-4">
  <div class="title" style="top:11px">What Makes Brivento Numérica Unique?</div>
  <div class="rule" style="top:28px"></div>
  <div class="table-box">
    <div class="th" style="left:44px;width:68px;justify-content:center">Feature</div>
    <div class="th" style="left:118px;width:274px;padding-left:16px">Description</div>
    <div class="trow" style="top:21px"><div class="ico"><svg viewBox="0 0 24 24" fill="none" stroke="#27998b" stroke-width="2"><circle cx="12" cy="10" r="6"/><path d="M9 19h6M10 22h4M12 1v2M3 10H1M23 10h-2"/></svg></div><div class="feat">Innovative Lesson Design</div><div class="desc">Our lessons are designed for 1 ½-hour sessions, each covering a new math concept that can be taught in 20 minutes, allowing students ample time to practice the newly introduced math skills daily.</div></div>
    <div class="trow" style="top:46px"><div class="ico"><svg viewBox="0 0 24 24" fill="#27998b"><rect x="8" y="2" width="15" height="11" rx="1"/><circle cx="5" cy="9" r="3"/><path d="M1 22v-6a4 4 0 0 1 8 0v6z"/></svg></div><div class="feat">Comprehensive Math Teaching</div><div class="desc">Comprehensive online math curriculum teaching service for independently schooled students in grades 6 through 12 worldwide.</div></div>
    <div class="trow" style="top:71px"><div class="ico"><svg viewBox="0 0 24 24" fill="none" stroke="#27998b" stroke-width="2"><path d="M2 5h8l2 3h10v13H2z"/><path d="M8 14h8M8 17h5"/></svg></div><div class="feat">Effective Curricula</div><div class="desc">Time-tested and proven pedagogical methodology with three pillars: (1) new math concepts built on previously taught ones; (2) daily review of earlier math concepts to increase understanding; and (3) frequent, cumulative assessments to ensure students master each math skill as new ones are added.</div></div>
    <div class="trow" style="top:96px"><div class="ico"><svg viewBox="0 0 24 24" fill="#27998b"><circle cx="12" cy="5" r="3"/><path d="M6 9h12v3h-4v5h-4v-5H6z"/><rect x="3" y="19" width="18" height="3"/></svg></div><div class="feat">Engagement and Mastery</div><div class="desc">We are invested in your child's long-term success. We are not a tutoring service that provides a patchwork of sessions without a clear vision or goal. We are a complete online math curriculum and virtual classroom teaching service. We aim to have your child master mathematics, build their confidence, problem-solving skills, and love of learning.</div></div>
    <div class="trow" style="top:121px"><div class="ico"><svg viewBox="0 0 24 24" fill="none" stroke="#27998b" stroke-width="2"><rect x="4" y="2" width="16" height="20" rx="2"/><circle cx="12" cy="12" r="4"/><path d="M10.5 12l1.2 1.2 2.3-2.4M8 5h8"/></svg></div><div class="feat">Frequent Assessments</div><div class="desc">Access to over twenty cumulative tests per grade. Tests are scheduled so that students have 5 days to practice the concepts before being assessed. Each test comes with a Facts Practice given at the beginning.</div></div>
    <div class="trow" style="top:146px"><div class="ico"><svg viewBox="0 0 24 24" fill="#27998b"><rect x="2" y="2" width="12" height="8"/><circle cx="5" cy="14" r="2.5"/><circle cx="12" cy="14" r="2.5"/><circle cx="19" cy="14" r="2.5"/><path d="M1 23v-4a4 4 0 0 1 8 0v4zM8 23v-4a4 4 0 0 1 8 0v4zM15 23v-4a4 4 0 0 1 8 0v4z"/></svg></div><div class="feat">Synchronous Class Sessions</div><div class="desc">Real-time teacher-student interactions. Teaching is done through our math academy, a one-on-one, virtual adaptive classroom that uses integrated, interactive digital whiteboards for both teachers and students.</div></div>
  </div>
  <footer class="footer"><div class="brand"><span class="brand-dot"></span>Brivento Numérica</div><span class="copy">© Copyrights 2026 | All Rights Reserved</span></footer>
  <span class="page-num">04</span>
</section>

<section class="slide col-r row-1">
  <div class="title" style="top:11px">How Brivento Numérica Works</div>
  <div class="rule" style="top:30px"></div>
  <div class="abs" style="left:0;width:449px;top:50px;text-align:center;font-family:'Outfit',sans-serif;font-weight:600;font-size:11.5px;color:var(--teal)">Teacher’s View</div>
  <div class="step" style="left:65px"><div class="step-ring"><svg viewBox="0 0 24 24" fill="#27998b"><circle cx="10" cy="7" r="5"/><path d="M1 22a9 8 0 0 1 14-6.5V22z"/><path d="M19 13v8M15 17h8" stroke="#27998b" stroke-width="2.4"/></svg></div><h4>Create Lesson and Setup Class</h4><p>Name it, select grade/topic</p></div>
  <div class="step" style="left:145px"><div class="step-ring"><svg viewBox="0 0 24 24" fill="#27998b"><rect x="2" y="6" width="20" height="4"/><rect x="4" y="10" width="3" height="11"/><rect x="17" y="10" width="3" height="11"/><rect x="8" y="11" width="8" height="5"/><rect x="7" y="2" width="10" height="3" rx="1"/></svg></div><h4>Invite Students</h4><p style="margin-top:10px">Share a class code or link</p></div>
  <div class="step" style="left:224px"><div class="step-ring"><svg viewBox="0 0 24 24" fill="#27998b"><path d="M6 17l2-5L19 1l4 4-11 11z"/><path d="M2 22h20" stroke="#27998b" stroke-width="1.5" stroke-dasharray="2 2"/></svg></div><h4>Launch Session</h4><p style="margin-top:10px">Start a live whiteboard and teach a lesson</p></div>
  <div class="step" style="left:304px"><div class="step-ring"><svg viewBox="0 0 24 24" fill="#27998b"><rect x="9" y="2" width="6" height="5"/><rect x="11" y="7" width="2" height="4"/><rect x="4" y="11" width="16" height="2"/><rect x="4" y="11" width="2" height="5"/><rect x="11" y="11" width="2" height="5"/><rect x="18" y="11" width="2" height="5"/><rect x="2" y="16" width="6" height="5"/><rect x="9" y="16" width="6" height="5"/><rect x="16" y="16" width="6" height="5"/></svg></div><h4>Interact in Real Time</h4><p style="margin-top:10px;width:62px">Students write/draw alongside the teacher</p></div>
  <div class="step" style="left:383px"><div class="step-ring"><svg viewBox="0 0 24 24" fill="#27998b"><rect x="6" y="2" width="15" height="17" rx="1"/><path d="M3 5v17h15v-2H5V5z"/><path d="M11 7v7l5-3.5z" fill="#fff"/></svg></div><h4>Review Work</h4><p style="margin-top:10px">Teachers give comments or assign practice</p></div>
  <svg class="arrow" style="left:97px" viewBox="0 0 16 6"><path d="M0 3h13M11 .5L15 3l-4 2.5" stroke="#222" stroke-width="1" fill="none"/></svg>
  <svg class="arrow" style="left:177px" viewBox="0 0 16 6"><path d="M0 3h13M11 .5L15 3l-4 2.5" stroke="#222" stroke-width="1" fill="none"/></svg>
  <svg class="arrow" style="left:256px" viewBox="0 0 16 6"><path d="M0 3h13M11 .5L15 3l-4 2.5" stroke="#222" stroke-width="1" fill="none"/></svg>
  <svg class="arrow" style="left:336px" viewBox="0 0 16 6"><path d="M0 3h13M11 .5L15 3l-4 2.5" stroke="#222" stroke-width="1" fill="none"/></svg>
  <footer class="footer"><div class="brand"><span class="brand-dot"></span>Brivento Numérica</div><span class="copy">© Copyrights 2026 | All Rights Reserved</span></footer>
  <span class="page-num">05</span>
</section>

<section class="slide col-r row-2">
  <div class="title" style="top:12px">Section Divider</div>
  <div class="rule" style="top:30px"></div>
  <footer class="footer"><div class="brand"><span class="brand-dot"></span>Brivento Numérica</div><span class="copy">© Copyrights 2026 | All Rights Reserved</span></footer>
  <span class="page-num">06</span>
</section>

<section class="slide col-r row-3">
  <div class="title" style="top:12px">Who Is Brivento For?</div>
  <div class="rule" style="top:30px"></div>
  <div class="card" style="left:26px">
    <div class="card-head">Target Users</div>
    <ul class="ticks">
      <li>English-speaking grades 6–12 independently schooled students worldwide</li>
      <li>Working parents of grades 6–12 independently schooled students</li>
      <li>Internationally travelling parents with grades 6–12 independently schooled students</li>
      <li>Remote schools that are struggling to find qualified grade 6-12 math teachers</li>
    </ul>
  </div>
  <div class="card" style="left:228px">
    <div class="card-head">Opportunity</div>
    <ul class="ticks">
      <li>Over 4 million independently schooled students in English-speaking countries: USA 3+ million; Canada 100,000; UK 57,000; and Australia 30,000</li>
      <li>Shortage of qualified mathematics teachers and tutors</li>
      <li>Latin America + U.S + Canada have a high demand for bilingual math education</li>
      <li>Math is consistently the most challenging subject in middle and high schools</li>
    </ul>
  </div>
  <footer class="footer"><div class="brand"><span class="brand-dot"></span>Brivento Numérica</div><span class="copy">© Copyrights 2026 | All Rights Reserved</span></footer>
  <span class="page-num">07</span>
</section>

<section class="slide col-r row-4">
  <div class="board-art" role="img" aria-label="Illustration of a classroom whiteboard with coloured magnets, markers and a sponge on its tray"></div>
  <div class="board-logo" style="top:94px">
    <div class="brand" style="font-size:8.5px"><span class="brand-dot" style="width:8px;height:8px"></span>Brivento Numérica</div>
    <div class="tagline" style="font-size:3.4px">Inspiring Math • Empowering Learning</div>
  </div>
  <div class="title" style="top:119px;font-size:25px;font-weight:700">Thank You</div>
  <div class="rule" style="top:152px"></div>
</section>

</body>
</html>
```